Tervo's Glen

I need a Bussiness Card for my new company in Miami Beach, my company is based in Winwood Miami and all around me is arts soo I would like my card with stripes, art design.

Artists, Actress, actors, show bussiness

It Company

• Art Design

```html
<!DOCTYPE html>
<html lang="en">
<head>
<meta charset="utf-8">
<title>Tervo's Glen — Business Card</title>
<link rel="stylesheet" href="https://fonts.googleapis.com/css2?family=Open+Sans:wght@400;600;700;800&display=swap">
<style>
  :root {
    --backdrop: #e9e7e4;
    --card-white: #ffffff;
    --card-grey: #e4e4e4;
    --maroon: #74262b;
    --stripe-red: #c3243a;
    --name-red: #b8233a;
    --ink: #3a3a3a;
    --contact-white: #ffffff;
  }
  * { box-sizing: border-box; margin: 0; padding: 0; }
  html, body {
    width: 1200px; height: 900px; overflow: hidden;
    background: var(--backdrop);
    font-family: "Open Sans", Arial, sans-serif;
  }
  .canvas {
    width: 1200px; height: 900px;
    display: flex; align-items: center; justify-content: center;
  }
  .card {
    position: relative;
    width: 900px; height: 520px;
    border-radius: 44px;
    overflow: hidden;
    background: radial-gradient(ellipse at 55% 30%, var(--card-white) 0%, #f6f6f6 45%, var(--card-grey) 100%);
    box-shadow: 0 10px 30px rgba(0,0,0,0.18);
  }
  .card__swoosh { position: absolute; inset: 0; width: 100%; height: 100%; }
  .brand {
    position: absolute; left: 356px; top: 108px;
    display: flex; align-items: center; gap: 12px;
    white-space: nowrap;
  }
  .brand__dot {
    width: 26px; height: 26px; border-radius: 50%;
    background: var(--maroon);
    flex: none;
  }
  .brand__name {
    font-weight: 800; font-size: 40px; line-height: 1;
    color: var(--maroon); letter-spacing: -0.5px;
  }
  .person {
    position: absolute; right: 230px; top: 220px; text-align: right;
    white-space: nowrap;
  }
  .person__name {
    font-weight: 700; font-size: 22px; color: var(--name-red);
  }
  .person__role {
    font-weight: 400; font-size: 20px; color: var(--ink); margin-top: 4px;
  }
  .contact {
    position: absolute; left: 46px; top: 372px;
    color: var(--contact-white); font-size: 15px; line-height: 1.45;
  }
  .contact__lines { list-style: none; }
  .contact__lines + .contact__lines { margin-top: 10px; }
</style>
</head>
<body>
<main class="canvas">
  <section class="card">
    <svg class="card__swoosh" viewBox="0 0 900 520" preserveAspectRatio="none" aria-hidden="true">
      <path fill="var(--stripe-red)"
        d="M-10,282 C240,366 450,398 560,370 C705,332 772,190 782,-10 L910,-10 L910,530 L-10,530 Z"/>
      <path fill="var(--maroon)" stroke="#ffffff" stroke-width="3"
        d="M-10,286 C250,382 450,414 570,386 C720,350 790,200 802,-10 L910,-10 L910,530 L-10,530 Z"/>
    </svg>

    <div class="brand">
      <span class="brand__dot"></span>
      <span class="brand__name">Tervo's Glen</span>
    </div>

    <div class="person">
      <p class="person__name">Mira Kallstrom</p>
      <p class="person__role">Consultant</p>
    </div>

    <div class="contact">
      <ul class="contact__lines">
        <li>P : 012 555 0147</li>
        <li>F : 012 555 0148</li>
      </ul>
      <ul class="contact__lines">
        <li>hello@tervosglen.com</li>
        <li>www.tervosglen.com</li>
        <li>27 Canvas Lane, 2nd floor, Wynwood</li>
      </ul>
    </div>
  </section>
</main>
</body>
</html>
```